New nutrition counseling business needs a flyer and logo design for marketing purposes

Need a new flyer for distribution to advertise and inform the public about new Dietetic Counseling service. The new business name is Harbor of Vitality with “Harbor” being the main name. It will provide nutrition consultation services to individuals who seek to change their dietary habits to achieve a variety of different health objectives. These objectives can include, but are not limited to weight management, enhanced athletic performance, improved health biomarkers, and reducing the risks or symptoms of chronic nutrition related diseases. The services provided include direct one on one counseling that entails health and nutrition assessments, evaluation of goals, and the determination of strategies to meet these goals. We would like to see designs that use an ocean color scheme with purple aspects as well. Color and logo ideas attached in uploads. Please include logo on the flyer as well.

Target Market(s)

General Population

Colors
0094D4
00A9DD
6FCCEA
C7EBF8
E9F6FB
00AB8E
00BBA5
67D7C9
C6EFE9
E9F9F6
6B429C
8869AF
B7A5CE
E3DAEB
F3F0F8

Requirements
Nice to have
• Pictures of nourishing foods, fruits, vegetables etc.
Should not have
• Do not include people in flyer or logo design

```html
<!DOCTYPE html>
<html lang="en">
<head>
<meta charset="utf-8">
<title>Harbor of Vitality – Nutrition Counseling Flyer</title>
<link rel="stylesheet" href="https://fonts.googleapis.com/css2?family=Oswald:wght@300;400&family=Dancing+Script:wght@400;500&family=Open+Sans:wght@400;600;700&display=swap">
<style>
  :root {
    --teal-deep: #1fbcc8;
    --teal-title: #2cb2c6;
    --teal-pill: #6dcfd6;
    --teal-soft: #c9ecef;
    --teal-logo: #8fd7dc;
    --teal-script: #1a9fa6;
    --ink: #4f4f4f;
    --ink-soft: #7a7a7a;
    --paper: #ffffff;
  }
  html, body {
    margin: 0;
    padding: 0;
    width: 1035px;
    height: 1200px;
    overflow: hidden;
    background: var(--paper);
  }
  .flyer {
    position: relative;
    width: 1035px;
    height: 1200px;
    overflow: hidden;
    background: var(--paper);
    font-family: "Open Sans", sans-serif;
    color: var(--ink);
  }
  .flyer-shapes {
    position: absolute;
    inset: 0;
  }
  .tagline-script {
    position: absolute;
    left: 74px;
    top: 372px;
    margin: 0;
    font-family: "Dancing Script", cursive;
    font-size: 28px;
    color: var(--ink-soft);
  }
  .headline {
    position: absolute;
    left: 46px;
    top: 496px;
    margin: 0;
    font-family: "Oswald", sans-serif;
    font-weight: 300;
    font-size: 40px;
    line-height: 58px;
    color: var(--teal-title);
  }
  .services-title {
    position: absolute;
    left: 46px;
    top: 632px;
    margin: 0;
    font-family: "Oswald", sans-serif;
    font-weight: 300;
    font-size: 56px;
    letter-spacing: 1px;
    color: var(--teal-title);
  }
  .services-list {
    position: absolute;
    left: 46px;
    top: 712px;
    margin: 0;
    padding: 0;
    list-style: none;
    font-size: 19px;
    line-height: 31px;
    color: var(--ink);
  }
  .services-list li {
    padding-left: 20px;
    position: relative;
  }
  .services-list li::before {
    content: "•";
    position: absolute;
    left: 0;
  }
  .consult-pill {
    position: absolute;
    left: 32px;
    top: 982px;
    width: 578px;
    height: 64px;
    border-radius: 32px;
    background: var(--teal-pill);
    color: var(--paper);
    font-family: "Oswald", sans-serif;
    font-weight: 300;
    font-size: 27px;
    line-height: 64px;
    text-align: center;
    margin: 0;
  }
  .brand {
    position: absolute;
    left: 700px;
    top: 440px;
    width: 280px;
    display: flex;
    flex-direction: column;
    align-items: center;
    gap: 14px;
  }
  .brand-dot {
    width: 150px;
    height: 150px;
    border-radius: 50%;
    background: var(--teal-logo);
    border: 6px solid var(--paper);
  }
  .brand-name {
    margin: 0;
    font-family: "Oswald", sans-serif;
    font-weight: 300;
    font-size: 34px;
    line-height: 40px;
    color: var(--teal-title);
    text-align: center;
  }
  .chat-block {
    position: absolute;
    left: 615px;
    top: 712px;
    width: 360px;
    text-align: center;
    font-family: "Dancing Script", cursive;
  }
  .chat-title {
    margin: 0;
    font-size: 48px;
    font-weight: 400;
    color: var(--ink);
    line-height: 66px;
  }
  .chat-offer {
    margin: 6px 0 0;
    font-size: 25px;
    line-height: 38px;
    color: var(--teal-script);
  }
  .contact {
    position: absolute;
    right: 34px;
    top: 1050px;
    text-align: right;
    color: var(--paper);
    font-style: normal;
  }
  .contact-name {
    margin: 0;
    font-family: "Oswald", sans-serif;
    font-weight: 300;
    font-size: 27px;
    line-height: 36px;
  }
  .contact-name small {
    font-family: "Open Sans", sans-serif;
    font-weight: 600;
    font-size: 13px;
  }
  .contact-license {
    margin: 0;
    font-size: 15px;
    font-weight: 600;
    line-height: 24px;
    padding-right: 4px;
  }
  .contact-line {
    margin: 4px 0 0;
    font-size: 21px;
    font-weight: 700;
    line-height: 28px;
    display: flex;
    align-items: center;
    justify-content: flex-end;
    gap: 10px;
  }
  .contact-line svg {
    width: 22px;
    height: 22px;
  }
</style>
</head>
<body>
<main class="flyer">
  <svg class="flyer-shapes" width="1035" height="1200" viewBox="0 0 1035 1200">
    <defs>
      <linearGradient id="foodBoardTones" x1="0" y1="0" x2="1" y2="1">
        <stop offset="0" stop-color="#5a4636"/>
        <stop offset="0.35" stop-color="#8a6b4f"/>
        <stop offset="0.6" stop-color="#c9b89c"/>
        <stop offset="0.85" stop-color="#7c6a55"/>
        <stop offset="1" stop-color="#4f4033"/>
      </linearGradient>
      <linearGradient id="produceTones" x1="0" y1="0" x2="1" y2="0">
        <stop offset="0" stop-color="#b83a2a"/>
        <stop offset="0.3" stop-color="#7ea33a"/>
        <stop offset="0.55" stop-color="#e0a52b"/>
        <stop offset="0.8" stop-color="#a9c466"/>
        <stop offset="1" stop-color="#c84a32"/>
      </linearGradient>
      <linearGradient id="sideProduceTones" x1="0" y1="0" x2="0" y2="1">
        <stop offset="0" stop-color="#6f9c3c"/>
        <stop offset="0.45" stop-color="#e59a2d"/>
        <stop offset="1" stop-color="#9bbb55"/>
      </linearGradient>
    </defs>

    <rect class="food-photo" x="0" y="0" width="1035" height="620" fill="url(#foodBoardTones)" role="img" aria-label="Photo of a wooden board with cheeses, berries, cured meats, dried apricots, olives and crackers"/>
    <rect class="side-produce-photo" x="990" y="560" width="45" height="290" fill="url(#sideProduceTones)" role="img" aria-label="Photo of fresh citrus, tomatoes and leafy greens"/>

    <path class="tagline-band" d="M0,352 C170,330 340,352 520,480 L0,480 Z" fill="var(--teal-soft)"/>
    <path class="content-panel" d="M0,442 C210,455 380,345 590,440 C700,490 800,560 990,560 L990,860 L1035,860 L1035,1200 L0,1200 Z" fill="var(--paper)"/>

    <rect class="produce-photo" x="0" y="1092" width="560" height="108" fill="url(#produceTones)" role="img" aria-label="Photo of a row of fresh fruits and vegetables"/>

    <path class="contact-arc-light" d="M540,1200 C620,1030 800,945 1035,932 L1035,1200 Z" fill="var(--teal-soft)"/>
    <path class="contact-panel" d="M570,1200 C650,1050 820,968 1035,958 L1035,1200 Z" fill="var(--teal-deep)"/>
  </svg>

  <p class="tagline-script">One on One Counseling</p>

  <h1 class="headline">Helping clients foster positive<br>nutrition practices for a healthier lifestyle</h1>

  <h2 class="services-title">SERVICES</h2>
  <ul class="services-list">
    <li>Medical Nutrition Therapy for chronic conditions such<br>as diabetes, hypertension, high cholesterol, and more</li>
    <li>Weight Management</li>
    <li>Healthy Eating and Meal Planning</li>
    <li>Nutrition for Athletic Performance</li>
    <li>Pre and Post Natal Nutrition</li>
    <li>Personalized meal plans uniquely catered to each individual</li>
    <li>Highly collaborative approach to help you meet your goals</li>
  </ul>

  <p class="consult-pill">IN PERSON &amp; VIRTUAL CONSULTATIONS ARE OFFERED</p>

  <div class="brand">
    <span class="brand-dot" aria-hidden="true"></span>
    <p class="brand-name">Harbor of Vitality</p>
  </div>

  <section class="chat-block">
    <h3 class="chat-title">Let’s Chat!</h3>
    <p class="chat-offer">Free 15-minute introductory<br>consultation to discuss program<br>details and rates</p>
  </section>

  <address class="contact">
    <p class="contact-name">MAREN OKAFOR <small>MS, RD, LD/N</small></p>
    <p class="contact-license">License Number:&nbsp; ND 40721.</p>
    <p class="contact-line">555-014-2270
      <svg viewBox="0 0 24 24" aria-hidden="true"><circle cx="12" cy="12" r="10.5" fill="none" stroke="#fff" stroke-width="2"/><path d="M8.6 6.8c.4-.3 1-.2 1.2.2l1 2c.2.4.1.8-.2 1.1l-.7.6c.6 1.3 1.6 2.3 2.9 2.9l.6-.7c.3-.3.7-.4 1.1-.2l2 1c.4.2.5.8.2 1.2l-.9 1.1c-.4.5-1.1.7-1.7.5-3.1-1-5.5-3.4-6.5-6.5-.2-.6 0-1.300.5-1.7z" fill="#fff"/></svg>
    </p>
    <p class="contact-line">maren@okafornutri.net
      <svg viewBox="0 0 24 24" aria-hidden="true"><circle cx="12" cy="12" r="11" fill="#fff"/><rect x="6" y="8" width="12" height="8.5" rx="1" fill="var(--teal-deep)"/><path d="M6.5 8.6 12 12.8l5.5-4.2" fill="none" stroke="#fff" stroke-width="1.4"/></svg>
    </p>
  </address>
</main>
</body>
</html>
```